I need a business card for myself, being a proprietor of a funeral parlor based in Manila. I'd like the card to have either of the following:
White Font on Black Background
or
Black Font on White Background
No logo is needed however I will appreciate any efforts to show a symbol of eternal happiness, aptly designed with above mentioned colors in mind.
Company name, address and contact on the lower right corner.
Logo or symbol anywhere.
Quillstone Funeral Services
+639174826351
darvik4521@pelmora.com
corner of Brisco Avenue and Velhurst Street
Makati City, Philippines
Thank you.
Update: Please include a small dove in your design. You are free to choose where you would like it on the card.

```html
<!DOCTYPE html>
<html lang="en">
<head>
<meta charset="utf-8">
<title>Quillstone Funeral Services – Business Card</title>
<link href="https://fonts.googleapis.com/css2?family=Libre+Baskerville&family=Jost:wght@300;400&display=swap" rel="stylesheet">
<style>
  :root {
    --backdrop: #e6e4e0;
    --card: #ffffff;
    --ink: #111111;
    --ink-soft: #3a3a3a;
    --pattern-tint: #ececec;
    --symbol-tone: #1a1a1a;
  }
  html, body {
    margin: 0;
    padding: 0;
    width: 1200px;
    height: 1024px;
    overflow: hidden;
    background: var(--backdrop);
  }
  .canvas {
    position: relative;
    width: 1200px;
    height: 1024px;
  }
  .card {
    position: absolute;
    left: 120px;
    top: 238px;
    width: 960px;
    height: 548px;
    background: var(--card);
    overflow: hidden;
    box-shadow: 0 10px 30px rgba(0,0,0,0.18);
  }
  .card__pattern {
    position: absolute;
    left: 420px;
    top: 0;
    width: 540px;
    height: 300px;
    background: linear-gradient(180deg, var(--pattern-tint), rgba(236,236,236,0.35));
  }
  .card__symbol {
    position: absolute;
    left: 86px;
    top: 150px;
    width: 172px;
    height: 172px;
    background: var(--symbol-tone);
  }
  .card__divider {
    position: absolute;
    left: 330px;
    top: 60px;
    width: 2px;
    height: 300px;
    background: var(--ink);
  }
  .card__info {
    position: absolute;
    left: 372px;
    top: 62px;
    color: var(--ink);
  }
  .company-name {
    font-family: "Libre Baskerville", Georgia, serif;
    font-size: 34px;
    font-weight: 400;
    margin: 0 0 26px;
    letter-spacing: 0.3px;
  }
  .contact {
    list-style: none;
    margin: 0;
    padding: 0;
    font-family: "Jost", "Futura", sans-serif;
    font-weight: 300;
    font-size: 25px;
    line-height: 34px;
    color: var(--ink-soft);
  }
  .contact__item {
    display: flex;
    align-items: flex-start;
    gap: 12px;
  }
  .contact__icon {
    flex: 0 0 20px;
    width: 20px;
    height: 20px;
    margin-top: 7px;
  }
  .card__band {
    position: absolute;
    left: 0;
    bottom: 0;
    width: 960px;
    height: 548px;
  }
</style>
</head>
<body>
<main class="canvas">
  <section class="card" aria-label="Business card for Quillstone Funeral Services">
    <div class="card__pattern" role="img" aria-label="Faint repeating eternal knot decoration"></div>

    <div class="card__symbol" role="img" aria-label="Endless knot symbol of eternal happiness"></div>

    <div class="card__divider"></div>

    <div class="card__info">
      <h1 class="company-name">Quillstone Funeral Services</h1>
      <ul class="contact">
        <li class="contact__item">
          <svg class="contact__icon" viewBox="0 0 20 20" aria-hidden="true">
            <circle cx="10" cy="10" r="8.5" fill="none" stroke="#111" stroke-width="1.6"/>
            <path d="M7 5.5l1.6 2.4-1 1.1c.6 1.3 1.6 2.3 2.9 2.9l1.1-1 2.4 1.6-.8 1.6c-3.6-.4-6.6-3.4-7-7z" fill="#111"/>
          </svg>
          <span>+63 917 482 6351</span>
        </li>
        <li class="contact__item">
          <svg class="contact__icon" viewBox="0 0 20 20" aria-hidden="true">
            <circle cx="10" cy="10" r="3.2" fill="none" stroke="#111" stroke-width="2"/>
            <path d="M13.2 7v4.2c0 1.6 2.8 1.6 2.8-.8A6 6 0 1 0 12.5 15.4" fill="none" stroke="#111" stroke-width="2"/>
          </svg>
          <span>darvik4521@pelmora.com</span>
        </li>
        <li class="contact__item">
          <svg class="contact__icon" viewBox="0 0 20 20" aria-hidden="true">
            <path d="M10 19s-6-6.4-6-10.5a6 6 0 0 1 12 0C16 12.6 10 19 10 19z" fill="#111"/>
            <circle cx="10" cy="8.5" r="2.2" fill="#fff"/>
          </svg>
          <span>Corner of Brisco Avenue and<br>Velhurst Street Makati City<br>Philippines</span>
        </li>
      </ul>
    </div>

    <svg class="card__band" viewBox="0 0 960 548" preserveAspectRatio="none" aria-hidden="true">
      <path d="M0 500 C 300 470, 640 420, 960 310 L960 548 L0 548 Z" fill="#111"/>
      <path d="M0 478 C 300 450, 640 400, 960 292 L960 300 C 640 410, 300 460, 0 490 Z" fill="#fff"/>
      <path d="M0 468 C 300 440, 640 390, 960 282 L960 292 C 640 400, 300 450, 0 478 Z" fill="#111"/>
    </svg>
  </section>
</main>
</body>
</html>
```